Re-design of Business Card

We require a design for our business card.

Korrim is a supplier of industrial packaging specializing in plastic products. We are undergoing a rebranding to appear more corporate. We have changed our company name to korrim and have a new logo.

I have uploaded our old card design with the previous company name.
Don't copy the current design. We are looking for a new design.

Industry/Entity Type

Manufacturing

Contact Information for Business Card

please don't copy the current design. we are looking for a new design.

Font styles to use
Sans Serif

Colors

Designer to choose colors to be used in the design.

Requirements
Must have
• clean and easy to read.

```html
<!DOCTYPE html>
<html lang="en">
<head>
<meta charset="UTF-8">
<title>Korrim Business Card</title>
<link rel="stylesheet" href="https://fonts.googleapis.com/css2?family=Poppins:wght@400;500;600&display=swap">
<style>
  :root {
    --white: #ffffff;
    --brand-orange: #f47f20;
    --charcoal: #4a3f38;
    --rust: #b04d0a;
    --rust-dark: #8a3905;
    --peach-start: #f6bfa0;
    --peach-end: #fde8d3;
    --text-light: #f2ece7;
  }
  html, body {
    margin: 0;
    padding: 0;
    width: 1200px;
    height: 777px;
    overflow: hidden;
    background: var(--white);
  }
  .card {
    position: relative;
    width: 1200px;
    height: 777px;
    font-family: "Poppins", sans-serif;
    background: var(--white);
    overflow: hidden;
  }
  .brand-name {
    position: absolute;
    left: 0;
    right: 0;
    top: 88px;
    text-align: center;
    font-size: 96px;
    font-weight: 600;
    color: var(--brand-orange);
    letter-spacing: 4px;
    line-height: 1.1;
    margin: 0;
  }
  .accent-stripe {
    position: absolute;
    left: 0;
    top: 289px;
    width: 1200px;
    height: 17px;
    background: linear-gradient(90deg, var(--peach-start) 0%, var(--peach-start) 45%, var(--peach-end) 55%, var(--peach-end) 100%);
  }
  .identity-band {
    position: absolute;
    left: 0;
    top: 306px;
    width: 1200px;
    height: 283px;
    background: var(--charcoal);
  }
  .person-name {
    position: absolute;
    left: 48px;
    top: 76px;
    margin: 0;
    font-size: 50px;
    font-weight: 500;
    letter-spacing: 3px;
    color: var(--brand-orange);
    line-height: 1.2;
  }
  .person-role {
    position: absolute;
    left: 53px;
    top: 146px;
    margin: 0;
    font-size: 22px;
    letter-spacing: 1.2px;
    color: var(--text-light);
  }
  .contact-list {
    position: absolute;
    left: 800px;
    top: 98px;
    margin: 0;
    padding: 0;
    list-style: none;
  }
  .contact-item {
    display: flex;
    align-items: center;
    height: 46px;
    font-size: 23px;
    letter-spacing: 1px;
    color: var(--text-light);
  }
  .contact-icon {
    width: 29px;
    height: 15px;
    margin-right: 24px;
    flex: none;
  }
  .office-band {
    position: absolute;
    left: 0;
    top: 589px;
    width: 1200px;
    height: 188px;
    background: var(--rust);
  }
  .office-title {
    position: absolute;
    left: 48px;
    top: 47px;
    margin: 0;
    font-size: 23px;
    font-weight: 600;
    letter-spacing: 2.5px;
    color: var(--text-light);
  }
  .office-badge {
    position: absolute;
    width: 42px;
    height: 42px;
    border-radius: 50%;
    background: var(--rust-dark);
    color: var(--text-light);
    font-size: 16px;
    font-weight: 600;
    display: flex;
    align-items: center;
    justify-content: center;
    top: 117px;
  }
  .badge-address { left: 47px; }
  .badge-fax { left: 561px; }
  .badge-web { left: 800px; }
  .address-street {
    position: absolute;
    left: 116px;
    top: 112px;
    margin: 0;
    font-size: 24px;
    letter-spacing: 2.5px;
    color: var(--text-light);
    line-height: 1.2;
  }
  .address-locality {
    position: absolute;
    left: 116px;
    top: 142px;
    margin: 0;
    font-size: 17px;
    letter-spacing: 2px;
    color: var(--text-light);
  }
  .office-detail {
    position: absolute;
    top: 126px;
    margin: 0;
    font-size: 17px;
    letter-spacing: 1px;
    color: var(--text-light);
  }
  .detail-fax { left: 635px; }
  .detail-web { left: 880px; }
</style>
</head>
<body>
  <div class="card">
    <h1 class="brand-name">KORRIM</h1>

    <div class="accent-stripe"></div>

    <section class="identity-band">
      <h2 class="person-name">Dana Whitford</h2>
      <p class="person-role">Machinery Sales Manager</p>
      <ul class="contact-list">
        <li class="contact-item">
          <svg class="contact-icon" viewBox="0 0 29 15" aria-hidden="true"><rect width="29" height="15" fill="#f2ece7"/></svg>
          +61 7 3045 2871
        </li>
        <li class="contact-item">
          <svg class="contact-icon" viewBox="0 0 29 15" aria-hidden="true"><rect width="29" height="15" fill="#f2ece7"/></svg>
          dana@korrim.com.au
        </li>
      </ul>
    </section>

    <section class="office-band">
      <h3 class="office-title">Head Office</h3>

      <span class="office-badge badge-address">A</span>
      <p class="address-street">48 Brennan St</p>
      <p class="address-locality">Wattle Park,Qld&nbsp;&nbsp;4127 Australia</p>

      <span class="office-badge badge-fax">F</span>
      <p class="office-detail detail-fax">1300 418 206</p>

      <span class="office-badge badge-web">W</span>
      <p class="office-detail detail-web">www.korrimpackaging.com.au</p>
    </section>
  </div>
</body>
</html>
```